BW Business Card

Used Car Sales
We are trying to recreate the image of our license plate on business cards,
it is a red background with a white oval that is open on the ends
I attempted to upload the image but it was a dismal failure when the products arrived
the lettering was too small and the edges were white
I think maybe the red needs some texture in it, still red but something that doesn't look so flat
and maybe a beveled edge around the white (not sure)

Target Market(s)

Adults 25-65 that drive

Industry/Entity Type

Business

Contact Information for Business Card

Rachel Thornbury, Sales Manager, BRIGHT WAY AUTO LOT, INC., 746 Ferris Lane, Pulaski, TN 38291,
931 555-0172 (office), 931 555-0849 (fax) - We Finance everyone with approved credit
BrightWayAutoLot.Com

On Back: Financing Available - We Finance everyone with approved credit
Easy Payments: Monthly, Semi-Monthly or Weekly
Ask about our Layaway plan
Open Mon-Sat
8:30 AM - 5 PM

Requirements
Must have
• We want to match the license plate (minus holes for screws)

```html
<!DOCTYPE html>
<html lang="en">
<head>
<meta charset="utf-8">
<title>Bright Way Auto Lot – Business Card</title>
<link rel="stylesheet" href="https://fonts.googleapis.com/css2?family=Crimson+Text:wght@400;600;700&display=swap">
<style>
  :root {
    --stage: #1c1c1c;
    --red-light: #f47a6a;
    --red: #e3161c;
    --red-deep: #a30d12;
    --red-dark: #7e070b;
    --oval: #dcddde;
    --ink: #141414;
    --highlight: #ffde00;
  }
  * { box-sizing: border-box; margin: 0; padding: 0; }
  html, body {
    width: 1200px;
    height: 900px;
    overflow: hidden;
    background: var(--stage);
    font-family: "Crimson Text", Georgia, serif;
    color: var(--ink);
  }
  .canvas { position: relative; width: 1200px; height: 900px; }

  .card {
    position: absolute;
    width: 560px;
    height: 320px;
    overflow: hidden;
  }
  .card--front { left: 90px; top: 130px; }
  .card--back { left: 550px; top: 470px; }

  .card__texture {
    position: absolute;
    inset: 0;
    background:
      radial-gradient(ellipse at 0% 0%, var(--red-light) 0%, transparent 45%),
      radial-gradient(ellipse at 0% 100%, var(--red-light) 0%, transparent 50%),
      linear-gradient(90deg, var(--red) 0%, var(--red) 45%, var(--red-deep) 80%, var(--red-dark) 100%);
  }
  .card__plate {
    position: absolute;
    inset: 0;
    width: 100%;
    height: 100%;
  }

  .card__content {
    position: absolute;
    inset: 0;
    display: flex;
    flex-direction: column;
    align-items: center;
    justify-content: center;
    text-align: center;
    line-height: 1.15;
  }

  /* Front */
  .contact__name { font-size: 21px; font-weight: 600; letter-spacing: 0.3px; }
  .contact__title { font-size: 16px; font-weight: 600; margin-top: 2px; }
  .company {
    margin-top: 22px;
    background: var(--highlight);
    border-radius: 10px;
    padding: 2px 8px 0;
    font-size: 31px;
    font-weight: 700;
    letter-spacing: 0.6px;
    white-space: nowrap;
  }
  .address { margin-top: 14px; font-size: 20px; font-weight: 600; }
  .phone { font-size: 16px; margin-top: 2px; }
  .phone:first-of-type { margin-top: 8px; }

  /* Back */
  .offer__headline { font-size: 22px; font-weight: 700; }
  .offer__terms { font-size: 12px; font-weight: 600; margin-top: 2px; }
  .offer__layaway { font-size: 19px; font-weight: 700; margin-top: 2px; }
  .hours { font-size: 22px; font-weight: 700; margin-top: 22px; }
  .website { font-size: 15px; font-weight: 700; margin-top: 12px; }
  .note { font-size: 15px; font-weight: 700; }
</style>
</head>
<body>
<main class="canvas">

  <section class="card card--front" aria-label="Business card front">
    <div class="card__texture" role="img" aria-label="Red textured square-grid background"></div>
    <svg class="card__plate" viewBox="0 0 560 320" preserveAspectRatio="none" aria-hidden="true">
      <ellipse cx="280" cy="166" rx="300" ry="143" fill="var(--red)"/>
      <ellipse cx="280" cy="158" rx="292" ry="136" fill="var(--red-deep)"/>
      <ellipse cx="280" cy="161" rx="290" ry="134" fill="var(--oval)"/>
    </svg>
    <div class="card__content">
      <p class="contact__name">RACHEL THORNBURY</p>
      <p class="contact__title">Sales Manager</p>
      <p class="company">BRIGHT WAY AUTO LOT, INC.</p>
      <p class="address">746 Ferris Lane, Pulaski, TN 38291</p>
      <p class="phone">931 555-0172 (office)</p>
      <p class="phone">931 555-0849 (fax)</p>
    </div>
  </section>

  <section class="card card--back" aria-label="Business card back">
    <div class="card__texture" role="img" aria-label="Red textured square-grid background"></div>
    <svg class="card__plate" viewBox="0 0 560 320" preserveAspectRatio="none" aria-hidden="true">
      <ellipse cx="280" cy="166" rx="300" ry="143" fill="var(--red)"/>
      <ellipse cx="280" cy="158" rx="292" ry="136" fill="var(--red-deep)"/>
      <ellipse cx="280" cy="161" rx="290" ry="134" fill="var(--oval)"/>
    </svg>
    <div class="card__content">
      <p class="offer__headline">We Finance everyone with approved credit!</p>
      <p class="offer__terms">Easy Payments: Monthly, Semi-Monthly or Weekly</p>
      <p class="offer__layaway">Ask about our Layaway plan</p>
      <p class="hours">Open Mon-Sat 8:30 AM - 5 PM</p>
      <p class="website">BrightWayAutoLot.Com</p>
      <p class="note">On Back: Financing Available</p>
    </div>
  </section>

</main>
</body>
</html>
```